Construction Business Card Design

We need a business card design for a new company based in Dallas/Ft Worth, Texas called Calloway Venn Construction. We are a commercial construction design/build general contractor. We construct warehouse, office, manufacturing, tenant improvements, tenant finish-out, remodeling.

Reason: Additional designs, would like to see one incorporating CV as logo but keep actual company name on card as well thanks

Target Market(s)

Developers/Business Owners

Industry/Entity Type

Construction

Contact Information for Business Card

CALLOWAY VENN CONSTRUCTION, Nolan Pritchett, 4817 FM 932, Ste 318, Bartonville, TX 76239 Mailing: 3728 Silver Hollow Road, Flower Mound, 75041,Office-940-555-0142, M-555-555-0187, F-555-555-0163, nolan@callowayvenn.example, www.callowayvenn.example

Requirements
Must have
• Color/Stand out/Unique
Nice to have
• Logo uploaded is a first shot at design but the mountain is not a requirement

```html
<!DOCTYPE html>
<html lang="en">
<head>
<meta charset="utf-8">
<title>Calloway Venn Construction — Business Card</title>
<link href="https://fonts.googleapis.com/css2?family=Libre+Baskerville:wght@400;700&display=swap" rel="stylesheet">
<style>
  :root {
    --backdrop: #d9d9d9;
    --card-white: #ffffff;
    --card-black: #050505;
    --navy: #1f2a80;
    --ink: #2b2b2b;
    --blue-light: #1ea0e6;
    --blue-deep: #0b4fa8;
    --band-black: #1a1a1a;
    --band-grey: #8a8a8a;
    --silver: #e6e6e6;
  }
  * { box-sizing: border-box; margin: 0; padding: 0; }
  html, body { width: 1200px; height: 1000px; overflow: hidden; }
  body {
    background: var(--backdrop);
    font-family: "Libre Baskerville", Georgia, serif;
    display: flex;
    flex-direction: column;
    align-items: center;
    justify-content: center;
    gap: 60px;
  }
  .card {
    position: relative;
    width: 700px;
    height: 400px;
    overflow: hidden;
    box-shadow: 0 6px 20px rgba(0,0,0,0.18);
  }
  .card--front { background: var(--card-white); }
  .card--back {
    background: var(--card-black);
    display: flex;
    align-items: center;
    justify-content: center;
  }
  .bottom-bands { position: absolute; left: 0; bottom: 0; width: 700px; height: 120px; }

  .wordmark { color: var(--navy); font-weight: 400; line-height: 1.15; white-space: nowrap; }
  .card--front .wordmark {
    position: absolute;
    left: 40px;
    top: 60px;
    font-size: 24px;
    letter-spacing: 0.5px;
  }
  .wordmark__sub { display: block; font-size: 14px; letter-spacing: 3px; margin-top: 6px; }

  .divider {
    position: absolute;
    left: 320px;
    top: 40px;
    width: 2px;
    height: 130px;
    background: var(--band-black);
  }

  .contact {
    position: absolute;
    left: 350px;
    top: 48px;
    color: var(--ink);
    font-size: 16px;
    line-height: 1.65;
  }
  .contact__name {
    color: var(--navy);
    font-weight: 700;
    font-size: 18px;
    letter-spacing: 1px;
    margin-bottom: 10px;
  }
  .contact__row { display: flex; }
  .contact__label {
    width: 34px;
    color: var(--navy);
    font-weight: 700;
    display: flex;
    justify-content: space-between;
    margin-right: 8px;
  }
  .contact__label::after { content: "|"; color: var(--ink); font-weight: 400; }
  .contact__indent { padding-left: 0; }

  .card--back .wordmark {
    color: var(--silver);
    font-size: 32px;
    text-align: center;
    letter-spacing: 1px;
  }
  .card--back .wordmark__sub { font-size: 17px; letter-spacing: 4px; }
</style>
</head>
<body>

  <section class="card card--front" aria-label="Business card front">
    <div class="wordmark">CALLOWAY VENN<span class="wordmark__sub">CONSTRUCTION</span></div>

    <span class="divider"></span>

    <div class="contact">
      <p class="contact__name">NOLAN PRITCHETT</p>
      <p class="contact__row"><span class="contact__label">M</span>555-555-0187</p>
      <p class="contact__row"><span class="contact__label">F</span>555-555-0163</p>
      <p class="contact__row"><span class="contact__label">A</span>3728 Silver Hollow Road</p>
      <p class="contact__indent">Maple Crest</p>
      <p class="contact__indent">99041</p>
    </div>

    <svg class="bottom-bands" viewBox="0 0 700 120" aria-hidden="true">
      <defs>
        <linearGradient id="band-blue" x1="0" y1="0" x2="1" y2="0">
          <stop offset="0" stop-color="#1ea0e6"/>
          <stop offset="1" stop-color="#0b4fa8"/>
        </linearGradient>
      </defs>
      <polygon points="0,70 190,70 215,40 700,40 700,120 0,120" fill="url(#band-blue)" transform="translate(0,28)"/>
      <polygon points="220,46 700,46 700,58 232,58" fill="#1a1a1a"/>
      <polygon points="232,58 700,58 700,64 236,64" fill="#8a8a8a"/>
    </svg>
  </section>

  <section class="card card--back" aria-label="Business card back">
    <div class="wordmark">CALLOWAY VENN<span class="wordmark__sub">CONSTRUCTION</span></div>
  </section>

</body>
</html>
```